Flyer for American Indian Elders on Dementia Warning Signs

We need a flyer designed for older adults who are American Indian or Alaska Native (in the U.S.).

Ideally, the flyer should complement the colors of our logos. The project logo and our organization logo are attached to the brief.

When people see the flyer we want them to feel that it represents their culture, is warm, and professional but relatable to older adults and people who have limited incomes.

I have attached an earlier draft of the document we designed ourselves BUT we want different and better.

It is for older adults who have trouble reading so:
1. you must use a font that is 11.5 points or larger
2. Do not put text over complex pictures or use shading with words
3. You can use a serif font for the heading, but should use san serif for the body text
4. There should be good contrast between the font color and background

Please do not use any images that include a head dress or pictures of American Indian people or things that are very traditional or "token" imagery.

We need to save a small space under the call out box/ somewhere on the flyer for other people to add their logo once they download.

Let us know if you have questions or need additional information.

Target Market(s)

Older American Indian people

Font styles to use
Serif
Sans Serif

Requirements
Must have
• Easy to read for older adults
Should not have
• indian headdress

```html
<!DOCTYPE html>
<html lang="en">
<head>
<meta charset="utf-8">
<title>10 Signs of Thinking or Memory Changes that Might be Dementia</title>
<link href="https://fonts.googleapis.com/css2?family=Roboto:ital,wght@0,400;0,700;1,400&family=Tinos:wght@400;700&display=swap" rel="stylesheet">
<style>
:root{
  --red:#ad5d54;
  --red-dark:#9c4c44;
  --teal:#52a8b0;
  --panel:#f4f4f4;
  --ink:#2b2b2b;
  --white:#ffffff;
  --stage:#e6e6e6;
}
*{box-sizing:border-box;margin:0;padding:0}
html,body{width:1200px;height:1180px;overflow:hidden;background:var(--stage)}
.flyer{position:absolute;left:144px;top:0;width:1160px;height:1501px;background:var(--white);
  transform:scale(0.786);transform-origin:0 0;font-family:'Roboto',sans-serif;color:var(--ink)}
.header{position:absolute;left:0;top:0;width:1160px;height:188px}
.header svg{position:absolute;left:0;top:0}
.title{position:absolute;left:55px;top:24px;font-family:'Tinos',serif;color:var(--white);font-size:40px;line-height:49px}
.title strong{font-size:54px;font-weight:700}
.title .or{font-size:40px}
.org-name{position:absolute;left:770px;top:60px;width:360px;font-family:'Roboto',sans-serif;font-weight:700;color:var(--red);font-size:28px;line-height:32px;text-align:right}
.intro{position:absolute;left:0;top:188px;width:1160px;height:181px;background:var(--teal);color:var(--white);
  padding:22px 33px;font-size:20.5px;line-height:27px}
.intro p+p{margin-top:20px}
.signs{position:absolute;left:0;top:369px;width:1160px;height:719px;background:var(--panel);border-radius:0 0 130px 130px}
.sign{position:absolute}
.num{position:absolute;left:-42px;top:0;width:31px;height:31px;border-radius:50%;background:var(--red);color:var(--white);
  font-family:'Tinos',serif;font-weight:700;font-size:20px;line-height:31px;text-align:center}
.sign h3,.sign .lead{font-family:'Tinos',serif;font-size:21px;line-height:27px;font-weight:400;color:var(--red)}
.sign h3 b{font-weight:700}
.sign .lead.dark{color:var(--ink)}
.bullets{list-style:none;margin-top:12px}
.bullets li{position:relative;padding-left:37px;font-size:21px;line-height:27px;margin-bottom:3px}
.bullets li svg{position:absolute;left:0;top:5px}
.points{position:absolute;left:50px;top:1133px;width:1060px;height:223px;background:var(--teal);border-radius:32px;color:var(--white)}
.points-label{position:absolute;left:475px;top:-22px;width:250px;height:50px;background:var(--red-dark);border:3px solid var(--white);
  border-radius:26px;font-family:'Tinos',serif;font-size:40px;line-height:42px;text-align:center;color:var(--white)}
.point{position:absolute;padding-left:38px;font-size:21px;line-height:27px;width:470px}
.point svg{position:absolute;left:0;top:4px}
.footer{position:absolute;left:50px;top:1395px;width:1060px;height:60px}
.learn{position:absolute;left:0;top:4px;font-style:italic;font-size:18px;line-height:23px}
.divider{position:absolute;top:0;width:2px;height:56px;background:var(--red)}
.urls{position:absolute;left:490px;top:0;width:280px;text-align:center;color:var(--red);font-size:21px;line-height:27px}
.partner{position:absolute;left:825px;top:0;display:flex;align-items:center;gap:12px}
.partner .dot{width:60px;height:60px;border-radius:50%;background:var(--teal)}
.partner span{font-weight:700;color:var(--teal);font-size:16px;line-height:19px;width:170px}
</style>
</head>
<body>
<main class="flyer">
  <header class="header">
    <svg width="1160" height="188" viewBox="0 0 1160 188" aria-hidden="true">
      <rect width="1160" height="188" fill="var(--red)"/>
      <polygon points="610,0 1160,0 1160,173 707,173" fill="var(--white)"/>
    </svg>
    <h1 class="title"><strong>10 Signs of Thinking</strong> <span class="or">or</span><br>Memory Changes that Might<br>be Dementia</h1>
    <div class="org-name">Council for Native<br>Elder Wellness</div>
  </header>

  <section class="intro">
    <p>As you get older, we may slow down a bit. This is a normal part of aging. Changes in memory or thinking that make it harder to get through the day, are not a normal part of aging. These may be early signs of dementia.</p>
    <p>Because American Indian and Alaska Native people have a high risk of dementia, it is important to know the warning signs. Do you have any of these 10 signs? If so, talk to your doctor.</p>
  </section>

  <section class="signs">
    <div class="sign" style="left:74px;top:38px;width:480px">
      <span class="num">1</span>
      <h3><b>Memory loss that affects your daily life.</b> You may:</h3>
      <ul class="bullets">
        <li><svg width="17" height="17" viewBox="0 0 17 17"><circle cx="8.5" cy="8.5" r="8.5" fill="var(--teal)"/><path d="M4.5 8.8l2.6 2.5 5-5" stroke="#fff" stroke-width="2" fill="none"/></svg>Forget events or important dates</li>
        <li><svg width="17" height="17" viewBox="0 0 17 17"><circle cx="8.5" cy="8.5" r="8.5" fill="var(--teal)"/><path d="M4.5 8.8l2.6 2.5 5-5" stroke="#fff" stroke-width="2" fill="none"/></svg>Repeat yourself</li>
        <li><svg width="17" height="17" viewBox="0 0 17 17"><circle cx="8.5" cy="8.5" r="8.5" fill="var(--teal)"/><path d="M4.5 8.8l2.6 2.5 5-5" stroke="#fff" stroke-width="2" fill="none"/></svg>Rely more often on lists or sticky notes to remember things</li>
      </ul>
    </div>
    <div class="sign" style="left:74px;top:204px;width:430px">
      <span class="num">2</span>
      <h3><b>Trouble planning or solving problems.</b> You may have a harder time:</h3>
      <ul class="bullets">
        <li><svg width="17" height="17" viewBox="0 0 17 17"><circle cx="8.5" cy="8.5" r="8.5" fill="var(--teal)"/><path d="M4.5 8.8l2.6 2.5 5-5" stroke="#fff" stroke-width="2" fill="none"/></svg>Paying bills</li>
        <li><svg width="17" height="17" viewBox="0 0 17 17"><circle cx="8.5" cy="8.5" r="8.5" fill="var(--teal)"/><path d="M4.5 8.8l2.6 2.5 5-5" stroke="#fff" stroke-width="2" fill="none"/></svg>Cooking recipes you have used for years</li>
      </ul>
    </div>
    <div class="sign" style="left:74px;top:350px;width:430px">
      <span class="num">3</span>
      <h3><b>Get confused about the time, date, or where you are.</b></h3>
    </div>
    <div class="sign" style="left:74px;top:418px;width:480px">
      <span class="num">4</span>
      <h3><b>Daily tasks are getting harder, including:</b></h3>
      <ul class="bullets">
        <li><svg width="17" height="17" viewBox="0 0 17 17"><circle cx="8.5" cy="8.5" r="8.5" fill="var(--teal)"/><path d="M4.5 8.8l2.6 2.5 5-5" stroke="#fff" stroke-width="2" fill="none"/></svg>Driving</li>
        <li><svg width="17" height="17" viewBox="0 0 17 17"><circle cx="8.5" cy="8.5" r="8.5" fill="var(--teal)"/><path d="M4.5 8.8l2.6 2.5 5-5" stroke="#fff" stroke-width="2" fill="none"/></svg>Making a grocery list or going shopping</li>
      </ul>
    </div>
    <div class="sign" style="left:74px;top:528px;width:500px">
      <span class="num">5</span>
      <h3><b>Trouble with how your eyesight and thinking work together that gets worse. This includes:</b></h3>
      <ul class="bullets" style="margin-top:16px">
        <li><svg width="17" height="17" viewBox="0 0 17 17"><circle cx="8.5" cy="8.5" r="8.5" fill="var(--teal)"/><path d="M4.5 8.8l2.6 2.5 5-5" stroke="#fff" stroke-width="2" fill="none"/></svg>Tripping, falls, or problems with your balance</li>
        <li><svg width="17" height="17" viewBox="0 0 17 17"><circle cx="8.5" cy="8.5" r="8.5" fill="var(--teal)"/><path d="M4.5 8.8l2.6 2.5 5-5" stroke="#fff" stroke-width="2" fill="none"/></svg>Spilling or dropping things more</li>
      </ul>
    </div>

    <div class="sign" style="left:618px;top:37px;width:500px">
      <span class="num">6</span>
      <p class="lead dark"><b style="color:var(--red)">New trouble talking or writing.</b> You have a hard time finding the words you want to say. For example, you may say “that thing on your wrist that tells time” instead of “watch.”</p>
    </div>
    <div class="sign" style="left:618px;top:157px;width:520px">
      <span class="num">7</span>
      <h3><b>Lose and cannot find things. For example, you:</b></h3>
      <ul class="bullets">
        <li><svg width="17" height="17" viewBox="0 0 17 17"><circle cx="8.5" cy="8.5" r="8.5" fill="var(--teal)"/><path d="M4.5 8.8l2.6 2.5 5-5" stroke="#fff" stroke-width="2" fill="none"/></svg>Can't find the coffee pot that you use every day</li>
        <li><svg width="17" height="17" viewBox="0 0 17 17"><circle cx="8.5" cy="8.5" r="8.5" fill="var(--teal)"/><path d="M4.5 8.8l2.6 2.5 5-5" stroke="#fff" stroke-width="2" fill="none"/></svg>Might put your car keys in the freezer</li>
      </ul>
    </div>
    <div class="sign" style="left:618px;top:265px;width:530px">
      <span class="num">8</span>
      <p class="lead dark"><b style="color:var(--red)">Notice changes in mood or personality,</b> such as being:</p>
      <ul class="bullets" style="margin-top:16px">
        <li><svg width="17" height="17" viewBox="0 0 17 17"><circle cx="8.5" cy="8.5" r="8.5" fill="var(--teal)"/><path d="M4.5 8.8l2.6 2.5 5-5" stroke="#fff" stroke-width="2" fill="none"/></svg>Easily mad or sad in everyday situations</li>
        <li><svg width="17" height="17" viewBox="0 0 17 17"><circle cx="8.5" cy="8.5" r="8.5" fill="var(--teal)"/><path d="M4.5 8.8l2.6 2.5 5-5" stroke="#fff" stroke-width="2" fill="none"/></svg>More fearful (scared) or suspicious (not trusting)</li>
      </ul>
    </div>
    <div class="sign" style="left:618px;top:382px;width:530px">
      <span class="num">9</span>
      <p class="lead dark"><b style="color:var(--red)">Act different and make poor choices.</b> This may<br>make you more likely to:</p>
      <ul class="bullets" style="margin-top:16px">
        <li><svg width="17" height="17" viewBox="0 0 17 17"><circle cx="8.5" cy="8.5" r="8.5" fill="var(--teal)"/><path d="M4.5 8.8l2.6 2.5 5-5" stroke="#fff" stroke-width="2" fill="none"/></svg>Spend money you do not have or be a scam victim</li>
        <li><svg width="17" height="17" viewBox="0 0 17 17"><circle cx="8.5" cy="8.5" r="8.5" fill="var(--teal)"/><path d="M4.5 8.8l2.6 2.5 5-5" stroke="#fff" stroke-width="2" fill="none"/></svg>Stop washing up regularly or pay less attention to how you look</li>
        <li><svg width="17" height="17" viewBox="0 0 17 17"><circle cx="8.5" cy="8.5" r="8.5" fill="var(--teal)"/><path d="M4.5 8.8l2.6 2.5 5-5" stroke="#fff" stroke-width="2" fill="none"/></svg>Forget to take care of your pet</li>
      </ul>
    </div>
    <div class="sign" style="left:618px;top:580px;width:480px">
      <span class="num">10</span>
      <p class="lead dark"><b style="color:var(--red)">Pull away from friends and family because it is harder to keep up.</b> You may not want to do things you used to enjoy, like sporting events, church, music, or sex.</p>
    </div>
  </section>

  <section class="points">
    <h2 class="points-label">Main Points</h2>
    <div class="point" style="left:28px;top:46px"><svg width="25" height="25" viewBox="0 0 25 25"><circle cx="12.5" cy="12.5" r="11" stroke="#fff" stroke-width="2" fill="none"/><path d="M7.5 12.8l3.5 3.5 7-8" stroke="#fff" stroke-width="2" fill="none"/></svg>American Indian and Alaska Native people have a high risk of dementia.</div>
    <div class="point" style="left:28px;top:117px"><svg width="25" height="25" viewBox="0 0 25 25"><circle cx="12.5" cy="12.5" r="11" stroke="#fff" stroke-width="2" fill="none"/><path d="M7.5 12.8l3.5 3.5 7-8" stroke="#fff" stroke-width="2" fill="none"/></svg>People with one or more of these 10 signs should talk to their doctor to find the cause. It is not always dementia.</div>
    <div class="point" style="left:520px;top:44px"><svg width="25" height="25" viewBox="0 0 25 25"><circle cx="12.5" cy="12.5" r="11" stroke="#fff" stroke-width="2" fill="none"/><path d="M7.5 12.8l3.5 3.5 7-8" stroke="#fff" stroke-width="2" fill="none"/></svg>Early dementia diagnosis gives you a chance to get care and plan your future.</div>
    <div class="point" style="left:520px;top:117px"><svg width="25" height="25" viewBox="0 0 25 25"><circle cx="12.5" cy="12.5" r="11" stroke="#fff" stroke-width="2" fill="none"/><path d="M7.5 12.8l3.5 3.5 7-8" stroke="#fff" stroke-width="2" fill="none"/></svg>Big changes in memory or thinking that make it hard to get through the day are not a normal part of aging.</div>
  </section>

  <footer class="footer">
    <p class="learn">To learn more about the warning signs of dementia<br>in American Indian and Alaska Native people, visit:</p>
    <span class="divider" style="left:470px"></span>
    <div class="urls">www.nativeeldersbrain.org<br>www.healthyagingnet.org/aging</div>
    <span class="divider" style="left:790px"></span>
    <div class="partner"><span class="dot"></span><span>Native Elders Brain Health Center</span></div>
  </footer>
</main>
</body>
</html>
```